依頼詳細
◇サイトマップ
①Home
② MENU&PRICE
③ SALON INFO
④ PRODUCTS
⑤ COUPON
⑥ GALLERY
⑦ STAFF
⑧ MOVI
⑨ RECRUIT
⑩ CONTACT
⑪BLOG(一覧)
⑫NEWS(一覧)
⑬アクセサリー

◇優先事項
1.ユーザビリティー
2.デザイン
3.編集更新

◇効果
1.新規顧客の獲得
2.売上の向上
3.認知度向上(情報発信)

◇ターゲット
男性客は多いので、集客は女性をメインにしたい。
30~40代をメインだが、20代の人もターゲットに入る
会社員、自営業など全体的に伸ばしたい。

◇提供素材
ロゴデータなし。
店舗内装に写真はある。
動画もとっているものがある。

◇sns
フェイスブック
ツイッター
ラインアット
をしている。

◇その他アプリ
メール予約のシステムを使っている

◇デザイン
シンプル  3   複雑
単色    4~5 カラフル
暗い    4   明るい
日常    1   高級
遊び心  1~2  厳粛
未来的  1~2  伝統的
女性   1    男性

◇テイスト
モダン・アンティーク・レトロなデザインが好き
フォーマル・幻想的・神秘的・知性的はイメージと違う

◇カラー
ベースは白やクリーム系
サロンの雰囲気に合わせて茶色やその他の差し色

◇参考サイト
特に無いが、情報がしっかり発信出来るサイトがベスト。
サイトURL
http://www.velvora-style.com/
ページ数
1ページ
希望イメージ
シンプル 複雑
単色 カラフル
暗い 明るい
日常 高級
遊び心 厳粛
未来的 伝統的
女性的 男性的
希望する色
茶系、 ベースは白やクリーム系 サロンの雰囲気に合わせて茶色やその他の差し色
納品ファイル
• イラストレーター形式 (.ai)
• フォトショップ形式 (.psd)
• PNG形式 (.png)
補足説明
◇素材
1.現行のサイトに有る写真やテキストは自由に使って頂いて構いません。

2.この度素材として撮影をしているものを、ソラデポットにてダウンロードしてお使い下さい。
http://soradepot.net/download/7b2e41d09a5c8f3e6d1a2b4c9e0f57a8d6c3b1e2
パスワード kiro

3.当店にてピクスナを契約していますのでその中から使用して一旦カンプ画像を入れておいて下さい。
https://jp.pixuna-stock.com/

※その他は商用利用可能な無料のものをお使い下さい。
もう少し提案が見たいため延長させて頂きます。
もう少し提案を頂ければと思います。
何卒宜しくお願い致します。
もう少しデザインを見てみたいため延長させていただきます。
宜しくお願い致します。

ひと目見て気に入りました。

素早い対応ありがとうございました。

```html
<!DOCTYPE html>
<html lang="ja">
<head>
<meta charset="utf-8">
<title>Velvora</title>
<link href="https://fonts.googleapis.com/css2?family=Noto+Sans+JP:wght@400;500;700&family=Noto+Serif+JP:wght@400;600;700&display=swap" rel="stylesheet">
<style>
:root{
  --brown-dark:#3a2416;
  --brown:#5a3a24;
  --gold:#c9a35a;
  --cream:#f7f3ec;
  --grey-band:#eceae6;
  --text:#3b3b3b;
  --muted:#777;
  --line:#d8d4cc;
  --white:#fff;
}
*{margin:0;padding:0;box-sizing:border-box}
html,body{width:1200px;height:3120px;overflow:hidden}
body{font-family:"Noto Sans JP",sans-serif;color:var(--text);background:var(--white);position:relative}

/* header */
.site-header{position:absolute;top:0;left:0;width:1200px;height:80px;background:linear-gradient(#4a2f1d,var(--brown-dark));display:flex;align-items:center;padding:0 170px}
.brand{display:flex;align-items:center;gap:10px;color:var(--gold);font-family:"Noto Serif JP",serif;font-weight:700;font-size:24px;line-height:1;white-space:nowrap}
.brand-mark{width:14px;height:14px;background:var(--gold)}
.header-info{margin-left:24px;color:#f0e6d4;font-size:10px;line-height:1.5;white-space:nowrap}
.header-info .tel{font-size:20px;color:var(--gold);font-weight:700;font-family:"Noto Serif JP",serif}
.global-nav{margin-left:auto;display:flex;gap:22px;color:#f0e6d4;font-size:11px;letter-spacing:.08em}

/* hero */
.hero{position:absolute;top:80px;left:0;width:1200px;height:360px;background:linear-gradient(135deg,#e9e2d6 0%,#cdbfae 40%,#b07a5a 70%,#e6ddd0 100%)}

/* concept */
.concept{position:absolute;top:380px;left:220px;width:760px;height:540px;background:var(--white);text-align:center;padding-top:40px}
.concept h1{font-family:"Noto Serif JP",serif;font-size:26px;font-weight:600;letter-spacing:.1em}
.concept .en{font-size:11px;color:var(--muted);letter-spacing:.2em;margin-top:4px}
.concept .rule{width:620px;height:1px;background:var(--line);margin:22px auto}
.concept .lead{font-family:"Noto Serif JP",serif;font-size:17px;line-height:1.9}
.concept .body{font-size:12px;line-height:2;color:#555;margin-top:24px}
.btn{display:inline-block;border:1px solid #555;padding:8px 24px;font-size:11px;letter-spacing:.1em;margin-top:26px;background:var(--white)}

/* tiles */
.tiles{position:absolute;top:940px;left:172px;width:856px;display:grid;grid-template-columns:repeat(3,1fr);grid-auto-rows:190px;gap:4px}
.tile{position:relative;color:var(--white);text-align:center;padding-top:36px}
.tile::after{content:"";position:absolute;inset:0;background:rgba(30,20,12,.45)}
.tile>*{position:relative;z-index:1}
.tile h3{font-family:"Noto Serif JP",serif;font-weight:400;font-size:16px;letter-spacing:.15em}
.tile p{font-size:10px;line-height:1.8;margin-top:14px;opacity:.9}
.tile .more{display:inline-block;border:1px solid #fff;font-size:9px;padding:4px 22px;margin-top:16px}
.t1{background:linear-gradient(#8a7a68,#5b4d40)}
.t2{background:linear-gradient(#c7b493,#8a7652)}
.t3{background:linear-gradient(#7b7a74,#4f4c46)}
.t4{background:linear-gradient(#6f5f55,#403530)}
.t5{background:linear-gradient(#9b8a74,#5a4d3f)}
.t6{background:linear-gradient(#7d7467,#4c4239)}

/* movie */
.diag-band{position:absolute;top:1320px;left:0}
.movie-title{position:absolute;top:1480px;left:0;width:1200px;text-align:center}
.movie-title h2{font-family:"Noto Serif JP",serif;font-weight:400;font-size:30px;letter-spacing:.1em}
.movie-title p{font-size:12px;color:var(--muted);margin-top:6px}
.videos{position:absolute;top:1590px;left:172px;width:856px;display:flex;justify-content:space-between}
.video{width:418px;text-align:center}
.video-frame{height:250px;border:1px solid var(--line);display:flex;align-items:center;justify-content:center;font-size:22px;font-weight:700;color:var(--text)}
.video figcaption{font-size:13px;margin-top:16px}

/* news */
.news{position:absolute;top:1990px;left:172px;width:856px;display:flex;justify-content:space-between}
.news-col{width:412px}
.news-col h2{font-size:13px;font-weight:500;letter-spacing:.05em;padding-bottom:10px;border-bottom:2px solid #555}
.news-col h2 span{font-size:10px;color:var(--muted);margin-left:6px}
.news-col li{list-style:none;font-size:11px;padding:11px 0;border-bottom:1px solid var(--line);display:flex;gap:14px}
.news-col li time{color:var(--muted)}
.news-col li::after{content:"›";margin-left:auto;color:var(--muted)}

/* sns */
.sns{position:absolute;top:2340px;left:0;width:1200px;height:330px;background:var(--grey-band);display:flex;justify-content:center;align-items:center;gap:40px}
.sns-box{width:408px;height:250px;background:var(--white);display:flex;align-items:center;justify-content:center;font-size:26px;font-weight:700;color:var(--text)}

/* footer */
.site-footer{position:absolute;top:2670px;left:0;width:1200px;height:450px;background:var(--cream)}
.foot-nav{text-align:center;font-size:11px;color:var(--muted);padding:30px 0 24px;border-bottom:1px solid var(--line);word-spacing:8px}
.foot-main{display:flex;align-items:flex-start;padding:34px 172px}
.foot-main .brand{color:var(--brown)}
.foot-main .brand-mark{background:var(--brown)}
.foot-addr{margin-left:24px;font-size:11px;line-height:1.8;color:#555}
.foot-addr .tel{font-size:22px;font-weight:700;color:var(--brown);font-family:"Noto Serif JP",serif}
.follow{margin-left:auto;text-align:right;font-size:11px;letter-spacing:.1em}
.follow .row{display:flex;gap:8px;margin-top:10px}
.follow .row span{border:1px solid var(--line);background:var(--white);padding:6px 18px;font-size:11px}
.copyright{position:absolute;bottom:0;left:0;width:1200px;height:60px;background:var(--brown-dark);color:#d9c9b0;font-size:10px;display:flex;align-items:center;justify-content:center}
</style>
</head>
<body>

<header class="site-header">
  <div class="brand"><span class="brand-mark"></span>Velvora</div>
  <div class="header-info">大阪市西区新町1-2-3 ベルヴォラビル1F<br><span class="tel">06-4821-3057</span><br>営業 10:00〜20:00 / 定休 火曜</div>
  <nav class="global-nav"><span>CONCEPT</span><span>GALLERY</span><span>STAFF</span><span>MENU</span><span>GALLERY</span><span>COUPON</span><span>VOICE</span><span>BLOG</span></nav>
</header>

<div class="hero" role="img" aria-label="サロン店内の写真：シャンプー台と赤いスタイリングチェア"></div>

<section class="concept">
  <h1>癒しの場としてのサロン</h1>
  <div class="en">CONCEPT</div>
  <div class="rule"></div>
  <p class="lead">安心のヘアケア知識と髪にやさしい厳選された薬剤<br>お客様にフィットするスタイル<br>落ち着いた空間<br>最新技術のエクステンション</p>
  <div class="rule" style="width:420px"></div>
  <p class="body">これまでたくさんのスタイルを届けてきました。<br>「ひとりひとりの時間を大切にしたい」そんな思いでお迎えしています。<br>こころも体もほっとできるサロンへ。</p>
  <p class="body" style="margin-top:14px">髪のダメージが気になる方、新しい自分に出会いたい方も、<br>ゆっくりとご相談ください。丁寧なカウンセリングから始めます。<br>スタッフ一同、心よりお待ちしております。</p>
  <span class="btn">CONCEPT PAGE</span>
</section>

<div class="tiles">
  <div class="tile t1" role="img" aria-label="コンセプトのイメージ写真"><h3>CONCEPT</h3><p>髪と心にやさしい<br>サロンづくりのこだわり</p><span class="more">MORE</span></div>
  <div class="tile t2" role="img" aria-label="サロンメニューのイメージ写真"><h3>SALON MENU</h3><p>カット・カラー・パーマ<br>各メニューと料金のご案内</p><span class="more">MORE</span></div>
  <div class="tile t3" role="img" aria-label="ヘアスタイルギャラリーの写真"><h3>GALLERY</h3><p>スタッフが手がけた<br>スタイルをご紹介</p><span class="more">MORE</span></div>
  <div class="tile t4" role="img" aria-label="クーポンのイメージ写真"><h3>COUPON</h3><p>初めての方に<br>お得なクーポン</p><span class="more">MORE</span></div>
  <div class="tile t5" role="img" aria-label="ブログのイメージ写真"><h3>BLOG</h3><p>サロンの日々と<br>最新情報をお届け</p><span class="more">MORE</span></div>
  <div class="tile t6" role="img" aria-label="お客様の声のイメージ写真"><h3>VOICE</h3><p>ご来店いただいた<br>お客様の声</p><span class="more">MORE</span></div>
</div>

<svg class="diag-band" width="1200" height="240" viewBox="0 0 1200 240"><polygon points="0,90 1200,0 1200,150 0,240" fill="#f0eeea"/></svg>

<div class="movie-title"><h2>MENU MOVIE</h2><p>オススメメニュー動画の紹介です。</p></div>

<div class="videos">
  <figure class="video"><div class="video-frame">Vidora</div><figcaption>最新技術で時短カラー</figcaption></figure>
  <figure class="video"><div class="video-frame">Vidora</div><figcaption>水素カラー＆水素トリートメント</figcaption></figure>
</div>

<section class="news">
  <div class="news-col">
    <h2>NEWS &amp; TOPICS<span>新着情報</span></h2>
    <ul>
      <li><time>2015.09.01</time>秋の新メニューのご案内です</li>
      <li><time>2015.08.25</time>夏季休業のお知らせ</li>
      <li><time>2015.08.18</time>ヘッドスパ体験キャンペーン</li>
      <li><time>2015.08.10</time>スタッフ募集のお知らせ</li>
      <li><time>2015.08.01</time>水素トリートメント導入しました</li>
    </ul>
  </div>
  <div class="news-col">
    <h2>STAFF BLOG<span>スタッフブログ</span></h2>
    <ul>
      <li><time>2015.09.03</time>水素カラーを体験してみました</li>
      <li><time>2015.08.29</time>秋のおすすめヘアスタイル</li>
      <li><time>2015.08.21</time>自宅でできるヘアケアのコツ</li>
      <li><time>2015.08.14</time>新しいスタイリング剤入荷</li>
      <li><time>2015.08.05</time>講習会に参加してきました</li>
    </ul>
  </div>
</section>

<section class="sns">
  <div class="sns-box">Sharebook</div>
  <div class="sns-box">Chirpline</div>
</section>

<footer class="site-footer">
  <div class="foot-nav">ホーム ｜ コンセプト ｜ メニュー ｜ サロン情報 ｜ 商品 ｜ クーポン ｜ ギャラリー ｜ スタッフ ｜ 動画 ｜ 求人 ｜ お問い合わせ ｜ ブログ ｜ ニュース</div>
  <div class="foot-main">
    <div class="brand"><span class="brand-mark"></span>Velvora</div>
    <div class="foot-addr">大阪市西区新町1-2-3 ベルヴォラビル1F<br><span class="tel">06-4821-3057</span><br>営業時間 10:00〜20:00<br>定休日 毎週火曜日</div>
    <div class="follow">FOLLOW US<div class="row"><span>Chirpline</span><span>Sharebook</span></div></div>
  </div>
  <div class="copyright">Copyright © Velvora All Rights Reserved.</div>
</footer>

</body>
</html>
```